Eavestone screen porch

Can you please design a flyer for me promoting my screen porch businessPlease remove the seamless gutters word from the title and add “screen porches” I have added the logo and a bunch of pictures from projects that I have done in the past. You can use words like Hillcrest Screen porches, etc

Target Market(s)

homeowners, contractors, builders

Industry/Entity Type

Construction

Requirements
Must have
• Dov Kerring
• Eavestone Gutters
• 2937 Old Hwy 52 N, Greer, SC 29607
• 864-307-6184
Nice to have
• A few colors maybe 3 most
• nice looking font

```html
<!DOCTYPE html>
<html lang="en">
<head>
<meta charset="utf-8">
<title>Eavestone Screen Porch Enclosures</title>
<link rel="stylesheet" href="https://fonts.googleapis.com/css2?family=Bebas+Neue&family=Montserrat:wght@400;500;600;700;800&family=Oswald:wght@500;600&display=swap">
<style>
  :root {
    --red: #d0182b;
    --red-dark: #a10f1e;
    --red-light: #e8293c;
    --ink: #231f20;
    --dark: #2a2728;
    --dark-2: #3a3637;
    --paper: #ffffff;
    --paper-2: #f1f1f1;
    --muted: #cfcfcf;
  }
  * { box-sizing: border-box; margin: 0; padding: 0; }
  html, body { width: 941px; height: 1200px; overflow: hidden; background: #e6e6e6; }
  body { font-family: "Montserrat", sans-serif; color: var(--ink); }

  .flyer { position: relative; width: 941px; height: 1200px; background: var(--paper); overflow: hidden; }

  /* header */
  .header { position: absolute; left: 0; top: 0; width: 941px; height: 175px; background: var(--paper); }
  .brand { position: absolute; left: 32px; top: 44px; display: flex; align-items: center; gap: 12px; }
  .brand-square { width: 22px; height: 22px; background: var(--ink); flex: none; }
  .brand-text { font-family: "Oswald", sans-serif; font-weight: 600; color: var(--ink); line-height: 1; }
  .brand-name { display: block; font-size: 50px; letter-spacing: 1px; }
  .brand-sub { display: block; font-size: 21px; letter-spacing: 4.6px; margin-top: 6px; }
  .title-banner { position: absolute; left: 372px; top: 47px; width: 569px; height: 108px; border-radius: 22px 0 0 22px;
    background: linear-gradient(180deg, var(--red-light), var(--red-dark)); display: flex; align-items: center; padding-left: 32px; }
  .title-banner h1 { font-family: "Bebas Neue", sans-serif; font-weight: 400; font-size: 54px; color: #fff; letter-spacing: 0.5px; text-shadow: 0 2px 3px rgba(0,0,0,.35); }
  .title-banner h1 b { font-family: "Oswald", sans-serif; font-weight: 600; font-size: 47px; letter-spacing: 0; }

  /* hero */
  .hero { position: absolute; left: 0; top: 175px; width: 941px; height: 354px; background: linear-gradient(90deg, var(--dark) 0%, var(--dark-2) 60%); }
  .hero-photo { position: absolute; left: 0; top: 0; width: 941px; height: 354px;
    background: linear-gradient(160deg, #b9bfc2 0%, #e9ecec 40%, #ffffff 55%, #8c7a63 85%, #6d5f4c 100%);
    clip-path: polygon(547px 0, 941px 0, 941px 354px, 412px 354px); }
  .hero-accents { position: absolute; left: 0; top: 0; }
  .hero-copy { position: absolute; left: 38px; top: 26px; width: 382px; color: #fff; }
  .hero-copy h2 { font-family: "Bebas Neue", sans-serif; font-weight: 400; font-size: 26px; line-height: 24px; letter-spacing: 0.2px; }
  .hero-copy h2 .accent { display: block; color: var(--red-light); font-family: "Oswald", sans-serif; font-weight: 600; font-size: 33px; line-height: 38px; letter-spacing: -0.5px; }
  .hero-copy p { margin-top: 16px; font-size: 13.4px; line-height: 18.8px; color: #f2f2f2; }

  /* project photos */
  .projects { position: absolute; left: 0; top: 529px; width: 941px; height: 232px; background: var(--paper); }
  .project { position: absolute; top: 23px; height: 205px; }
  .project-1 { left: 0; width: 322px; clip-path: polygon(0 0, 322px 0, 285px 205px, 0 205px);
    background: linear-gradient(170deg, #cfd8d8 0%, #4e4f4b 45%, #7d6a55 80%, #2f3a2a 100%); }
  .project-2 { left: 290px; width: 373px; clip-path: polygon(37px 0, 373px 0, 336px 205px, 0 205px);
    background: linear-gradient(175deg, #d9cfae 0%, #e4dcc3 30%, #3a3d45 55%, #d9d6cf 80%, #a79883 100%); }
  .project-3 { left: 631px; width: 310px; clip-path: polygon(37px 0, 310px 0, 310px 205px, 0 205px);
    background: linear-gradient(175deg, #c3d3e3 0%, #8f9196 35%, #5e6066 60%, #c8c9c4 80%, #6e8a4c 100%); }

  /* info */
  .info { position: absolute; left: 0; top: 761px; width: 941px; height: 277px; background: linear-gradient(180deg, var(--paper-2), #fafafa 40%, var(--paper)); }
  .why { position: absolute; left: 38px; top: 48px; width: 500px; }
  .kicker { font-size: 18.5px; font-weight: 500; color: var(--red); line-height: 22px; }
  .section-title { font-size: 18.5px; font-weight: 800; color: var(--ink); line-height: 23px; }
  .why p { margin-top: 12px; font-size: 14.3px; line-height: 20.4px; color: #333; }
  .why p + p { margin-top: 20px; }
  .divider { position: absolute; left: 573px; top: 46px; width: 1px; height: 212px; background: var(--muted); }
  .benefits { position: absolute; left: 614px; top: 46px; width: 300px; }
  .benefits .kicker { color: var(--ink); }
  .benefits .section-title { color: var(--red); }
  .benefit-list { list-style: none; margin-top: 10px; }
  .benefit-list li { display: flex; align-items: center; gap: 12px; height: 27.5px; font-size: 16.5px; font-weight: 600; color: var(--ink);
    background: linear-gradient(90deg, rgba(0,0,0,.05), rgba(0,0,0,0) 80%); margin-bottom: 1px; }
  .benefit-list svg { flex: none; }

  /* offer band */
  .offer { position: absolute; left: 0; top: 1038px; width: 941px; height: 54px; background: linear-gradient(180deg, var(--red-light), var(--red-dark));
    display: flex; align-items: center; justify-content: center; text-align: center; }
  .offer p { color: #fff; font-weight: 700; font-size: 14.8px; line-height: 20px; }

  /* footer */
  .footer { position: absolute; left: 0; top: 1092px; width: 941px; height: 108px; background: var(--dark); color: #fff; }
  .footer-phone { position: absolute; left: 48px; top: 17px; }
  .footer-label { font-size: 13.5px; font-weight: 800; color: var(--red-light); letter-spacing: 0.2px; }
  .phone-row { display: flex; align-items: center; gap: 10px; margin-top: 3px; }
  .phone-number { font-size: 33px; font-weight: 700; line-height: 34px; letter-spacing: -0.3px; }
  .phone-web { font-size: 13px; margin-left: 36px; margin-top: -3px; color: #eee; }
  .footer-sep { position: absolute; top: 25px; height: 64px; border-left: 2px dotted #6a6566; }
  .footer-item { position: absolute; top: 26px; text-align: center; font-size: 12px; font-weight: 600; line-height: 15.5px; }
  .footer-icon { width: 26px; height: 26px; background: var(--red); margin: 0 auto 10px; display: flex; align-items: center; justify-content: center; }
</style>
</head>
<body>
<main class="flyer">
  <header class="header">
    <div class="brand">
      <span class="brand-square"></span>
      <span class="brand-text">
        <span class="brand-name">EAVESTONE</span>
        <span class="brand-sub">SCREEN PORCHES</span>
      </span>
    </div>
    <div class="title-banner"><h1>SCREEN PORCH <b>ENCLOSURES</b></h1></div>
  </header>

  <section class="hero">
    <div class="hero-photo" role="img" aria-label="Photo of a white octagonal screened porch on posts with a white staircase, beside a house with light siding"></div>
    <svg class="hero-accents" width="941" height="354" viewBox="0 0 941 354">
      <polygon points="379,0 547,0 477,190" fill="#a10f1e"/>
      <polygon points="412,0 547,0 482,176" fill="#d0182b"/>
      <polygon points="440,0 547,0 488,160" fill="#e8293c"/>
    </svg>
    <div class="hero-copy">
      <h2>SCREENED-IN PORCH<br>ENCLOSURES IN GREENVILLE,<span class="accent">SPARTANBURG &amp; BEYOND!</span></h2>
      <p>Adding a screened in porch to your home helps maximize the size of your lot by creating more habitable space. You will be able to utilize your new porch almost all year round, especially with the predictive warm weather patterns of Greenville &amp; Spartanburg, SC. A screened in porch is something future homebuyers will be looking for within these areas due to their functionality; this in turn increases the value of your home. Choosing the right home improvements to invest in now will help you get the most return on your property when you do decide to sell.</p>
    </div>
  </section>

  <section class="projects">
    <div class="project project-1" role="img" aria-label="Photo of a gabled screened porch on a raised wooden deck with cable railing"></div>
    <div class="project project-2" role="img" aria-label="Photo of a screened porch with white railing and steps behind a tan house"></div>
    <div class="project project-3" role="img" aria-label="Photo of a ground-level screened porch on the back of a grey house"></div>
  </section>

  <section class="info">
    <div class="why">
      <div class="kicker">Why a</div>
      <div class="section-title">SCREENED-IN PORCH?</div>
      <p>Screen porch enclosures are beneficial to homes as they provide a quiet place to enjoy a good book, entertain friends and family at your next dinner party, or give the kids a safe place to play. What are some great things you could do with a screened in porch?</p>
      <p>If you're in Greenville, Spartanburg, or surrounding areas, call Eavestone Gutters today to start your project. We make homes more functional and comfortable, one screened in porch at a time!</p>
    </div>
    <div class="divider"></div>
    <div class="benefits">
      <div class="kicker">Benefits of</div>
      <div class="section-title">SCREENED-IN PORCH?</div>
      <ul class="benefit-list">
        <li><svg width="18" height="18" viewBox="0 0 17 17"><circle cx="8.5" cy="8.5" r="8.5" fill="#d0182b"/><path d="M4.6 8.8l2.6 2.5 5.2-5.4" stroke="#fff" stroke-width="2.2" fill="none"/></svg>Privacy</li>
        <li><svg width="18" height="18" viewBox="0 0 17 17"><circle cx="8.5" cy="8.5" r="8.5" fill="#d0182b"/><path d="M4.6 8.8l2.6 2.5 5.2-5.4" stroke="#fff" stroke-width="2.2" fill="none"/></svg>Year-Round Use</li>
        <li><svg width="18" height="18" viewBox="0 0 17 17"><circle cx="8.5" cy="8.5" r="8.5" fill="#d0182b"/><path d="M4.6 8.8l2.6 2.5 5.2-5.4" stroke="#fff" stroke-width="2.2" fill="none"/></svg>Extend Your Living Space</li>
        <li><svg width="18" height="18" viewBox="0 0 17 17"><circle cx="8.5" cy="8.5" r="8.5" fill="#d0182b"/><path d="M4.6 8.8l2.6 2.5 5.2-5.4" stroke="#fff" stroke-width="2.2" fill="none"/></svg>No Bugs</li>
        <li><svg width="18" height="18" viewBox="0 0 17 17"><circle cx="8.5" cy="8.5" r="8.5" fill="#d0182b"/><path d="M4.6 8.8l2.6 2.5 5.2-5.4" stroke="#fff" stroke-width="2.2" fill="none"/></svg>Home Value</li>
        <li><svg width="18" height="18" viewBox="0 0 17 17"><circle cx="8.5" cy="8.5" r="8.5" fill="#d0182b"/><path d="M4.6 8.8l2.6 2.5 5.2-5.4" stroke="#fff" stroke-width="2.2" fill="none"/></svg>New Family Space</li>
      </ul>
    </div>
  </section>

  <section class="offer">
    <p>We offer free estimates, so you may as well give us call us today to explore your<br>options of screened-in porches!</p>
  </section>

  <footer class="footer">
    <div class="footer-phone">
      <div class="footer-label">FOR MORE INFORMATION · DOV KERRING</div>
      <div class="phone-row">
        <svg width="26" height="38" viewBox="0 0 26 38"><rect x="2" y="2" width="22" height="34" rx="4" fill="none" stroke="#e8293c" stroke-width="3"/><line x1="9" y1="7" x2="17" y2="7" stroke="#e8293c" stroke-width="2"/><circle cx="13" cy="30" r="2" fill="#e8293c"/></svg>
        <span class="phone-number">864-307-6184</span>
      </div>
      <div class="phone-web">www.eavestoneseamlessgutters.com</div>
    </div>
    <div class="footer-sep" style="left:412px"></div>
    <div class="footer-item" style="left:436px;width:150px">
      <div class="footer-icon"><svg width="12" height="16" viewBox="0 0 12 16"><path d="M6 0a6 6 0 0 0-6 6c0 4.5 6 10 6 10s6-5.5 6-10a6 6 0 0 0-6-6z" fill="#2a2728"/><circle cx="6" cy="6" r="2.2" fill="#d0182b"/></svg></div>
      2937 Old Highway 52<br>North, Greer, SC 29607
    </div>
    <div class="footer-sep" style="left:606px"></div>
    <div class="footer-item" style="left:620px;width:212px">
      <div class="footer-icon"><svg width="14" height="14" viewBox="0 0 14 14"><circle cx="7" cy="7" r="6" fill="none" stroke="#2a2728" stroke-width="1.8"/><path d="M1 7h12M7 1c-3 3-3 9 0 12M7 1c3 3 3 9 0 12" stroke="#2a2728" stroke-width="1.2" fill="none"/></svg></div>
      info@eavestonegutters.com<br>www.eavestoneseamlessgutters.com
    </div>
  </footer>
</main>
</body>
</html>
```